Marlowe Hairdressing Business Card Design

The design has to be based upon a colour scheme of a black gloss background and silver type face letters and has to portray an exclusive and expensive outlet.

The business card has a dual use with the rear of the card being used for future appointments therefore this area has to be lined out to accept written text.

We also need to incorporate a Chatterbook log somewhere on the card.

Target Market(s)

High Earning individuals with high disposable incomes possible link too young professionals.

Contact Information for Business Card

Marlowe Hairdressing & The Willowmere Beauty
Tel 01632 418550
www.marlowehairdressing.example.co.uk

Requirements
Must have
• Company Name including beauty element, telephone number, website and chatterbook please.
Nice to have
• High Gloss finish with silver raised letters or similar
Should not have
• Hairdressing Images like, scissors, haircuts, beauty treatments etc

```html
<!DOCTYPE html>
<html lang="en">
<head>
<meta charset="utf-8">
<title>Marlowe Hairdressing – Business Card</title>
<link rel="stylesheet" href="https://fonts.googleapis.com/css2?family=Poiret+One&display=swap">
<style>
  :root {
    --page-bg: #ececec;
    --card-black: #050505;
    --silver-light: #e6e6e6;
    --silver-mid: #c4c4c4;
    --silver-dim: #a9a9a9;
    --frame-dark: #4a4a4a;
    --frame-light: #d9d9d9;
    --panel-light: #efefef;
    --panel-shade: #cfcfcf;
    --rule-line: #555555;
    --ink-grey: #5a5a5a;
  }
  * { margin: 0; padding: 0; box-sizing: border-box; }
  html, body {
    width: 1131px;
    height: 1200px;
    overflow: hidden;
    background: var(--page-bg);
    font-family: "Poiret One", sans-serif;
  }
  .canvas {
    position: relative;
    width: 1131px;
    height: 1200px;
  }
  .card {
    position: absolute;
    left: 205px;
    width: 720px;
    height: 411px;
    border-radius: 4px;
    box-shadow: 0 6px 18px rgba(0,0,0,0.18);
    overflow: hidden;
  }

  /* Appointment side */
  .card--appointments {
    top: 149px;
    background: linear-gradient(90deg, var(--frame-dark) 0%, var(--frame-light) 45%, var(--frame-light) 70%, var(--frame-dark) 100%);
  }
  .appointments-panel {
    position: absolute;
    inset: 26px 30px;
    background: linear-gradient(180deg, var(--panel-light) 0%, var(--panel-shade) 55%, var(--panel-light) 100%);
    padding: 26px 34px 0;
  }
  .appointments-title {
    font-size: 17px;
    color: var(--ink-grey);
    letter-spacing: 0.3px;
    white-space: nowrap;
  }
  .appointments-lines {
    position: absolute;
    left: 34px;
    right: 34px;
    top: 70px;
    width: calc(100% - 68px);
    height: 270px;
  }

  /* Contact side */
  .card--contact {
    top: 640px;
    background: var(--card-black);
    padding: 96px 50px 0;
    color: var(--silver-mid);
  }
  .contact-name {
    font-size: 29px;
    font-weight: 400;
    color: var(--silver-light);
    white-space: nowrap;
  }
  .contact-tel {
    margin-top: 14px;
    font-size: 26px;
    color: var(--silver-mid);
  }
  .contact-web {
    margin-top: 10px;
    font-size: 20px;
    color: var(--silver-mid);
  }
  .contact-social {
    margin-top: 44px;
    display: flex;
    align-items: center;
    gap: 12px;
    font-size: 19px;
    color: var(--silver-dim);
    white-space: nowrap;
  }
  .social-square {
    flex: none;
    width: 22px;
    height: 22px;
    background: var(--silver-dim);
    border-radius: 2px;
  }
</style>
</head>
<body>
<main class="canvas">

  <section class="card card--appointments" aria-label="Appointment card, rear">
    <div class="appointments-panel">
      <p class="appointments-title">Marlowe Hairdressing &amp; The Willowmere Beauty</p>
      <svg class="appointments-lines" viewBox="0 0 592 270" preserveAspectRatio="none" aria-hidden="true">
        <g stroke="var(--rule-line)" stroke-width="1.2">
          <line x1="0" y1="0" x2="592" y2="0"/>
          <line x1="0" y1="30" x2="592" y2="30"/>
          <line x1="0" y1="60" x2="592" y2="60"/>
          <line x1="0" y1="90" x2="592" y2="90"/>
          <line x1="0" y1="120" x2="592" y2="120"/>
          <line x1="0" y1="150" x2="592" y2="150"/>
          <line x1="0" y1="180" x2="592" y2="180"/>
          <line x1="0" y1="210" x2="592" y2="210"/>
          <line x1="0" y1="240" x2="592" y2="240"/>
          <line x1="0" y1="269" x2="592" y2="269"/>
        </g>
      </svg>
    </div>
  </section>

  <section class="card card--contact" aria-label="Business card, front">
    <h1 class="contact-name">Marlowe Hairdressing &amp; The Willowmere Beauty</h1>
    <p class="contact-tel">Tel 01632 418550</p>
    <p class="contact-web">www.marlowehairdressing.example.co.uk</p>
    <p class="contact-social"><span class="social-square" aria-hidden="true"></span>www.chatterbook.com/Marlowehairdressing</p>
  </section>

</main>
</body>
</html>
```